Poster Design for Photography Exhibit

We are looking for a poster design for a photography exhibit featuring high-end fashion and celebrity photography.

Name of the exhibit is "MILES DORVAN: UNTITLED" (please use Helvetica Black all cap for show name.

Poster is LANDSCAPE format (2 units wide by 1 unit high).

Unfortunately due to legal reasons, we cannot use any actual Miles Dorvan photos. No can we use fashions or people on the poster!

We are looking for a high-end, sexy, bold provocative design that captures the excitement and glamour of a fashion photo shoot.

Target Market(s)

Men and Women interested in Fashion Photography and art photography in general

Industry/Entity Type

Fashion

Requirements
Must have
• landscape format, name of exhibit in Helvetica Black all caps
Nice to have
• Can be grayscale or color.
Should not have
• Logos or brand names

```html
<!DOCTYPE html>
<html lang="en">
<head>
<meta charset="utf-8">
<title>Miles Dorvan : Untitled</title>
<link rel="stylesheet" href="https://fonts.googleapis.com/css2?family=Inter:wght@300;400;900&display=swap">
<style>
  :root {
    --paper: #ffffff;
    --ink: #000000;
    --text: #1a1a1a;
    --photo-dark: #050505;
    --photo-mid: #3a3a3a;
    --photo-light: #8c8c8c;
  }
  html, body {
    margin: 0;
    padding: 0;
    overflow: hidden;
    background: var(--paper);
  }
  .poster {
    position: relative;
    width: 1200px;
    height: 600px;
    overflow: hidden;
    background: var(--paper);
    font-family: "Inter", Arial, sans-serif;
    color: var(--text);
  }
  .site-url {
    position: absolute;
    left: 43px;
    top: 30px;
    font-size: 13px;
    font-weight: 400;
    margin: 0;
  }
  .title-band {
    position: absolute;
    left: 0;
    top: 133px;
    width: 800px;
    height: 206px;
    background: var(--ink);
  }
  .title-rule {
    position: absolute;
    left: 0;
    top: 227px;
    width: 800px;
    height: 4px;
    background: var(--paper);
  }
  .show-title {
    margin: 0;
    font-weight: 900;
    text-transform: uppercase;
    color: var(--paper);
  }
  .show-title .artist {
    position: absolute;
    left: 66px;
    top: 141px;
    font-size: 79px;
    line-height: 1;
    letter-spacing: -3px;
    white-space: nowrap;
  }
  .show-title .work {
    position: absolute;
    left: 56px;
    top: 226px;
    font-size: 136px;
    line-height: 1;
    letter-spacing: -4px;
    white-space: nowrap;
  }
  .blurb {
    position: absolute;
    right: 450px;
    top: 384px;
    margin: 0;
    text-align: right;
    font-size: 14.5px;
    line-height: 21.5px;
  }
  .blurb span { display: block; white-space: nowrap; }
  .dates {
    position: absolute;
    right: 450px;
    top: 488px;
    margin: 0;
    text-align: right;
    font-size: 27px;
    font-weight: 300;
    white-space: nowrap;
  }
  .dates-note {
    position: absolute;
    right: 450px;
    top: 519px;
    margin: 0;
    text-align: right;
    font-size: 13.5px;
    white-space: nowrap;
  }
  .feature-photo {
    position: absolute;
    left: 800px;
    top: 0;
    width: 400px;
    height: 600px;
  }
</style>
</head>
<body>
<main class="poster">
  <p class="site-url">www.dorvanexhibit.com</p>

  <div class="title-band"></div>
  <div class="title-rule"></div>
  <h1 class="show-title">
    <span class="artist">MILES DORVAN :</span>
    <span class="work">UNTITLED</span>
  </h1>

  <p class="blurb">
    <span>Lorem ipsum dolor sit amet, consectetur adipiscing elit. Curabitur si</span>
    <span>t amet lacus quis lectus suscipit mollis. Morbi varius ullamcorper fermentum. Nulla in nisi</span>
    <span>eu enim vulputate hendrerit. Nullam faucibus egestas molestie. Ut a libero at odio</span>
  </p>

  <p class="dates">7-27 June 2013, Location St.</p>
  <p class="dates-note">aucibus egestas molestie. Ut a libero at odio</p>

  <svg class="feature-photo" viewBox="0 0 400 600" role="img" aria-label="Black and white photograph of a vintage camera with its lens in close-up">
    <defs>
      <radialGradient id="photoGlow" cx="0.7" cy="0.58" r="0.6">
        <stop offset="0" stop-color="var(--photo-light)"/>
        <stop offset="0.35" stop-color="var(--photo-mid)"/>
        <stop offset="1" stop-color="var(--photo-dark)"/>
      </radialGradient>
    </defs>
    <rect width="400" height="600" fill="url(#photoGlow)"/>
  </svg>
</main>
</body>
</html>
```